KT Crewing business card

Require business card which includes:
Company name: KT CREWING PTY LTD
Email: Mick@ktcrewing.com.au
Phone: 0431 556 208
ACN: 517 238 649

slogan: Onsite Auto Electrician Labour hire

Details and logo on top side
Logo only on bottom side

colour codes : #F15A29 , #939598

Target Market(s)

Western Australia mining sector

Industry/Entity Type

Mining

Contact Information for Business Card

Require business card which includes: Company name: KT CREWING PTY LTD Email: Mick@ktcrewing.com.au Phone: 0431 556 208 ACN: 517 238 649 slogan: Onsite Auto Electrician Labour hire Details and logo on top side Logo only on bottom side colour codes : #F15A29 , #939598

Colors
EE7325
F08F49
F5BC92
FAE3D3
FDF4ED

Requirements
Must have
• double sided

```html
<!DOCTYPE html>
<html lang="en">
<head>
<meta charset="utf-8">
<title>KT Crewing — Business Card</title>
<link href="https://fonts.googleapis.com/css2?family=Archivo:wght@400;600;800&family=Michroma&display=swap" rel="stylesheet">
<style>
  :root {
    --backdrop: #e9e9e9;
    --card-dark: #313131;
    --card-deep: #1c1c1c;
    --card-mid: #4a4a4a;
    --orange: #F15A29;
    --grey: #939598;
    --white: #ffffff;
  }
  * { box-sizing: border-box; margin: 0; padding: 0; }
  html, body {
    width: 1200px; height: 802px; overflow: hidden;
    background: var(--backdrop);
    font-family: "Archivo", Arial, sans-serif;
  }
  .sheet {
    width: 1200px; height: 802px;
    display: flex; flex-direction: column; align-items: center; justify-content: center;
    gap: 40px;
  }
  .card {
    position: relative;
    width: 600px; height: 343px;
    border-radius: 4px;
    overflow: hidden;
    box-shadow: 0 6px 18px rgba(0,0,0,0.18);
  }

  /* Front */
  .card--front { background: var(--card-dark); }
  .brand {
    position: absolute; left: 150px; top: 80px;
    display: flex; align-items: center; gap: 14px;
  }
  .brand__square { width: 22px; height: 22px; background: var(--white); }
  .brand__name {
    font-weight: 800; font-size: 52px; line-height: 1;
    color: var(--orange); letter-spacing: 0.5px;
  }
  .details {
    position: absolute; left: 0; right: 0; top: 190px;
    display: flex; justify-content: center; align-items: stretch;
  }
  .person { text-align: right; padding-right: 20px; align-self: flex-end; }
  .person__name {
    color: var(--orange); font-size: 17px; font-weight: 600; letter-spacing: 0.5px;
  }
  .person__role { color: var(--white); font-size: 14px; margin-top: 3px; }
  .divider { width: 1px; background: var(--grey); }
  .contact { list-style: none; padding-left: 20px; }
  .contact__item {
    display: flex; align-items: center; gap: 8px;
    color: var(--white); font-size: 15px; line-height: 24px;
  }
  .contact__icon { width: 14px; height: 14px; fill: var(--orange); flex: none; }
  .contact__label { color: var(--orange); font-weight: 600; }

  /* Back */
  .card--back { background: var(--card-deep); }
  .back__art { position: absolute; inset: 0; }
  .back__brand {
    position: absolute; left: 40px; bottom: 34px;
    display: flex; align-items: center; gap: 10px;
  }
  .back__brand .brand__square { width: 16px; height: 16px; }
  .back__brand .brand__name { color: var(--white); font-size: 26px; }
  .slogan {
    position: absolute; right: 40px; bottom: 34px;
    font-family: "Michroma", Arial, sans-serif;
    color: var(--white); font-size: 14px; line-height: 19px;
    text-transform: uppercase; letter-spacing: 1px;
  }
</style>
</head>
<body>
<main class="sheet">

  <section class="card card--front" aria-label="Business card front">
    <div class="brand">
      <span class="brand__square"></span>
      <span class="brand__name">KT Crewing</span>
    </div>
    <div class="details">
      <div class="person">
        <p class="person__name">LIAM CARTER</p>
        <p class="person__role">Manager</p>
      </div>
      <span class="divider"></span>
      <ul class="contact">
        <li class="contact__item">
          <svg class="contact__icon" viewBox="0 0 24 24"><path d="M6.6 10.8a15.1 15.1 0 0 0 6.6 6.6l2.2-2.2a1 1 0 0 1 1-.25 11.4 11.4 0 0 0 3.6.57 1 1 0 0 1 1 1V20a1 1 0 0 1-1 1A17 17 0 0 1 3 4a1 1 0 0 1 1-1h3.5a1 1 0 0 1 1 1c0 1.25.2 2.45.57 3.57a1 1 0 0 1-.25 1z"/></svg>
          0431 556 208
        </li>
        <li class="contact__item">
          <svg class="contact__icon" viewBox="0 0 24 24"><path d="M2 5h20v14H2z M2 5l10 8 10-8" fill="var(--orange)"/><path d="M2 5l10 8 10-8" fill="none" stroke="var(--card-dark)" stroke-width="2"/></svg>
          Mick@ktcrewing.com.au
        </li>
        <li class="contact__item">
          <span class="contact__label">ACN</span> 517 238 649
        </li>
      </ul>
    </div>
  </section>

  <section class="card card--back" aria-label="Business card back">
    <svg class="back__art" role="img" aria-label="Large dark grey geometric brand decoration" viewBox="0 0 600 343" preserveAspectRatio="none">
      <defs>
        <linearGradient id="backShade" x1="0" y1="0" x2="1" y2="1">
          <stop offset="0" stop-color="#111111"/>
          <stop offset="0.55" stop-color="#2c2c2c"/>
          <stop offset="1" stop-color="#555555"/>
        </linearGradient>
      </defs>
      <rect width="600" height="343" fill="url(#backShade)"/>
    </svg>
    <div class="back__brand">
      <span class="brand__square"></span>
      <span class="brand__name">KT Crewing</span>
    </div>
    <p class="slogan">Onsite Auto<br>Electrician<br>Labour Hire</p>
  </section>

</main>
</body>
</html>
```